Industry automation wholesale website

www.velqora.eu provides solutions for automation, building automation and digital signage.

Our products are rugged, reliable, energy saving and representative.

Scope of pages:
● welcome page
- scope of products
- applications, success stories and news
● category page
- short introduction
- sub categories
- product highlights
● product page
- short introduction
- about 3 to 4 pictures
- technical specifications: materials, dimensions
- price
- related products

Optional:
● contact page
- address
- contact form
● blog
- picture
- text
● logo
● favicon / apple touch icon

Conclusion:
● We need a professionally looking site
● Bright colors (e.g. white, grey, metalic colors, blue)

some pages we like:
http://www.brundafel.de/
http://www.korvimash.de/

Target Market(s)

Our target market is the industrial sector
● Target audience: engineering and IT professionals

Industry/Entity Type

Building

Requirements
Must have
• ● only use free available fonts e.g. Pellor Type Library (http://www.pellortype.com/webfonts)
Should not have
• ● sound
● flash

```html
<!DOCTYPE html>
<html lang="en">
<head>
<meta charset="utf-8">
<title>velqora – Industry automation</title>
<link rel="stylesheet" href="https://fonts.googleapis.com/css2?family=Raleway:wght@400;500;600;700&family=Noto+Serif:ital@1&display=swap">
<style>
:root{
  --blue:#3d94c4;
  --blue-dark:#1f6f9e;
  --ink:#3b3f44;
  --text:#8a8f94;
  --muted:#b4b8bc;
  --line:#e3e6e8;
  --pale:#f1f7fc;
  --grey:#f1f2f2;
  --foot:#2c2d2d;
  --foot-text:#8b8d8d;
  --white:#ffffff;
}
*{box-sizing:border-box;margin:0;padding:0}
html,body{width:1200px;height:2576px;overflow:hidden;background:var(--white)}
body{font-family:"Raleway",Arial,sans-serif;color:var(--text);position:relative}
.abs{position:absolute}
p{font-size:11px;line-height:1.6}

/* header */
.site-header{position:absolute;top:0;left:0;width:1200px;height:50px;background:var(--white)}
.brand{left:325px;top:11px;display:flex;align-items:center;gap:5px;font-size:24px;font-weight:500;color:var(--blue-dark);letter-spacing:.5px;white-space:nowrap}
.brand-mark{width:9px;height:9px;border-radius:50%;background:var(--blue-dark);margin-top:-12px}
.main-nav{left:444px;top:22px;display:flex;gap:10px;font-size:8px;font-weight:600;color:var(--ink);white-space:nowrap}
.main-nav .active{color:var(--blue)}
.contact-bar{left:724px;top:20px;display:flex;gap:18px;font-size:8px;color:var(--blue);align-items:center;white-space:nowrap}
.contact-bar span{display:flex;align-items:center;gap:5px}

/* hero */
.hero{top:50px;left:0;width:1200px;height:341px;background:radial-gradient(ellipse at 75% 85%,#3f8f88 0%,#1d5a68 40%,#0f3a4d 75%,#0b2f41 100%)}
.hero-title{left:325px;top:130px;color:var(--white);font-size:17px;font-weight:700;line-height:1.2}
.hero-sub{left:325px;top:151px;color:#d9ecef;font-size:17px;font-weight:400;line-height:1.2}
.hero-text{left:325px;top:184px;width:225px;color:#b6d2d8;font-size:8.5px;line-height:1.55}
.btn-outline{display:flex;align-items:center;justify-content:center;border:1.5px solid var(--white);border-radius:16px;color:var(--white);font-size:10px;font-weight:700}
.hero-btn{left:326px;top:243px;width:112px;height:28px}
.hero-visual{left:430px;top:50px;width:440px;height:341px;background:linear-gradient(115deg,rgba(0,0,0,0) 20%,rgba(229,196,170,.5) 45%,rgba(40,30,60,.75) 62%,rgba(0,0,0,0) 80%)}

/* features */
.section-title{width:1200px;left:0;text-align:center;font-size:16px;font-weight:700;color:var(--ink);line-height:1.2}
.section-intro{left:420px;width:360px;text-align:center;font-size:8.5px;line-height:1.55}
.features-title{top:436px}
.features-intro{top:466px}
.feature-tabs{left:340px;top:530px;width:150px}
.feature-tab{height:53px;display:flex;align-items:center;gap:16px;font-size:10px;color:var(--muted);white-space:nowrap}
.feature-tab.current{color:var(--ink)}
.feature-divider{left:490px;top:520px;width:1px;height:282px;background:var(--line)}
.feature-marker{left:488px;top:591px;width:4px;height:36px;background:var(--blue)}
.feature-heading{left:559px;top:685px;font-size:11.5px;font-weight:700;color:var(--ink);line-height:1.2}
.feature-text{left:559px;top:710px;width:300px;font-size:8.5px;line-height:1.55}

/* key product */
.key-product{top:849px;left:0;width:1200px;height:383px;background:var(--pale)}
.blue-heading{font-size:16px;font-weight:700;color:var(--blue);line-height:1.3}
.rule{width:50px;height:1px;background:var(--blue)}
.key-heading{left:325px;top:921px;width:290px}
.key-rule{left:325px;top:971px}
.key-sub{left:325px;top:988px;width:230px;font-size:15px;font-weight:400;color:var(--text);line-height:1.35}
.key-text{left:325px;top:1046px;width:200px;font-size:8.5px;line-height:1.55}
.btn-blue{display:flex;align-items:center;justify-content:center;border:1.5px solid var(--blue);border-radius:16px;color:var(--ink);font-size:9.5px;font-weight:700;background:transparent}
.key-btn{left:326px;top:1115px;width:112px;height:28px}
.key-visual{left:660px;top:889px;width:146px;height:304px;border-radius:20px;background:linear-gradient(160deg,#f7a7c4,#e46f9c 55%,#c8577f)}

/* gallery */
.gallery-title{top:1277px}
.gallery-intro{top:1305px}
.gallery-item{top:1383px;width:154px}
.gallery-photo{width:154px;height:114px;background:linear-gradient(135deg,#5d7fa4,#3f5f83 60%,#8aa6c0)}
.gallery-badge{position:absolute;right:0;top:0;width:60px;height:20px;background:#d82b35}
.gallery-caption{margin:28px auto 0;width:110px;text-align:center;font-size:8px;line-height:1.5}
.gallery-arrow{top:1434px}

/* news */
.news{top:1611px;left:0;width:1200px;height:371px;background:var(--pale)}
.news-heading{left:325px;top:1678px;width:280px}
.news-rule{left:325px;top:1727px}
.news-col{top:1745px;width:255px}
.news-col h3{font-size:15px;font-weight:400;color:var(--text);margin-bottom:9px;line-height:1.2}
.news-col p{font-size:8.5px;line-height:1.55}
.news-btn{left:327px;top:1882px;width:113px;height:28px}

/* testimonial */
.testimonial-title{top:2048px}
.avatar{left:576px;top:2085px;width:46px;height:46px;border-radius:50%;background:radial-gradient(circle at 50% 40%,#d9a77e,#9a6a45 70%,#5c3f2a)}
.quote{left:0;width:1200px;top:2151px;text-align:center;font-family:"Noto Serif",Georgia,serif;font-style:italic;font-size:10.5px;color:var(--text)}
.quote-author{left:0;width:1200px;top:2175px;text-align:center;font-size:10.5px;color:var(--blue)}
.dots{left:588px;top:2206px;display:flex;gap:5px}
.dots i{width:4px;height:4px;border-radius:50%;background:var(--blue-dark);display:block}

/* newsletter */
.newsletter{top:2265px;left:0;width:1200px;height:168px;background:var(--grey)}
.newsletter-title{left:0;width:1200px;top:2304px;display:flex;justify-content:center;align-items:center;gap:9px;font-size:16px;font-weight:600;color:var(--muted);line-height:1.2}
.subscribe-form{left:420px;top:2348px;width:358px;height:28px;display:flex}
.subscribe-input{flex:1;border:1px solid #cfd3d6;border-right:none;border-radius:14px 0 0 14px;background:var(--white);font-size:8px;color:var(--muted);padding:9px 16px}
.subscribe-btn{width:78px;border-radius:14px;margin-left:-14px;background:var(--blue);color:var(--white);font-size:9.5px;font-weight:700;display:flex;align-items:center;justify-content:center}

/* footer */
.site-footer{top:2433px;left:0;width:1200px;height:143px;background:var(--foot)}
.footer-title{left:0;width:1200px;top:2464px;text-align:center;font-size:12px;color:var(--foot-text)}
.social{left:536px;top:2494px;display:flex;gap:10px}
.social i{width:18px;height:18px;border-radius:50%;background:#6a6c6c;display:block}
.footer-links{left:0;width:1200px;top:2543px;display:flex;justify-content:center;gap:12px;font-size:7.5px;color:var(--foot-text)}
</style>
</head>
<body>

<header class="site-header">
  <div class="abs brand">velqora<span class="brand-mark"></span></div>
  <nav class="abs main-nav"><span class="active">Home</span><span>Category</span><span>Products</span><span>Blog</span><span>Shopping Cart</span><span>Contacts</span></nav>
  <div class="abs contact-bar">
    <span><svg width="9" height="9" viewBox="0 0 10 10"><path d="M2 1h2l1 2.5-1.3.8a5 5 0 0 0 2 2l.8-1.3L9 6v2a1 1 0 0 1-1 1A7 7 0 0 1 1 2a1 1 0 0 1 1-1z" fill="#3b3f44"/></svg>+49 - 211 - 5520384</span>
    <span><svg width="10" height="8" viewBox="0 0 10 8"><rect x=".5" y=".5" width="9" height="7" rx="1" fill="none" stroke="#3b3f44"/><path d="M.5 1l4.5 3.5L9.5 1" fill="none" stroke="#3b3f44"/></svg>info@velqora.de</span>
  </div>
</header>

<section class="abs hero"></section>
<div class="abs hero-visual" role="img" aria-label="Hand holding a smartphone showing the automation app"></div>
<h1 class="abs hero-title">All about office automation</h1>
<h2 class="abs hero-sub">Go ahead with us</h2>
<p class="abs hero-text">Rugged controllers, panel PCs and signage players for plants and buildings. Energy saving hardware that keeps working year after year on site.</p>
<div class="abs btn-outline hero-btn">Read More</div>

<h2 class="abs section-title features-title">Checkout our features</h2>
<p class="abs section-intro features-intro">Discover the strengths behind our range of industrial products, built for engineers and IT professionals who need reliable hardware every single day.</p>

<div class="abs feature-tabs">
  <div class="feature-tab"><svg width="24" height="22" viewBox="0 0 24 22"><path d="M12 20S2 13.5 2 7.5A5 5 0 0 1 12 5a5 5 0 0 1 10 2.5C22 13.5 12 20 12 20z" fill="none" stroke="#9aa0a5" stroke-width="1.2"/></svg>Heading title one</div>
  <div class="feature-tab current"><svg width="24" height="22" viewBox="0 0 24 22"><rect x="2" y="6" width="20" height="13" rx="1.5" fill="none" stroke="#3d94c4" stroke-width="1.2"/><path d="M8 6V3h8v3M2 11h20" fill="none" stroke="#3d94c4" stroke-width="1.2"/><rect x="10" y="9.5" width="4" height="3" fill="#3d94c4"/></svg>Heading title one</div>
  <div class="feature-tab"><svg width="24" height="22" viewBox="0 0 24 22"><path d="M3 19C3 9 10 4 21 3c0 10-5 16-15 15M3 19l9-8" fill="none" stroke="#9aa0a5" stroke-width="1.2"/></svg>Heading title one</div>
  <div class="feature-tab"><svg width="24" height="22" viewBox="0 0 24 22"><rect x="8" y="2" width="9" height="18" rx="1.5" fill="none" stroke="#9aa0a5" stroke-width="1.2"/><path d="M8 5h9M8 16h9" stroke="#9aa0a5" stroke-width="1.2"/></svg>Heading title one</div>
  <div class="feature-tab"><svg width="24" height="22" viewBox="0 0 24 22"><path d="M3 12a9 8 0 0 1 18 0zM12 12v6a2 2 0 0 1-4 0" fill="none" stroke="#9aa0a5" stroke-width="1.2"/></svg>Heading title one</div>
</div>
<div class="abs feature-divider"></div>
<div class="abs feature-marker"></div>
<svg class="abs" style="left:656px;top:568px" width="98" height="84" viewBox="0 0 98 84"><rect x="2" y="14" width="94" height="68" rx="5" fill="none" stroke="#3d94c4" stroke-width="2"/><path d="M32 14V3h34v11M2 44h94" fill="none" stroke="#3d94c4" stroke-width="2"/><rect x="40" y="38" width="18" height="12" rx="2" fill="#fff" stroke="#3d94c4" stroke-width="2"/></svg>
<h3 class="abs feature-heading">Heading Feature title goes here</h3>
<p class="abs feature-text">Our panel PCs and controllers are built for cabinets, machine halls and public spaces. Fanless housings, wide temperature ranges and long term availability make planning simple. Each unit is tested before shipping and comes with clear documentation, so engineers can install, configure and maintain every device with confidence over many years.</p>

<section class="abs key-product"></section>
<h2 class="abs blue-heading key-heading">Get know about our key product that spread over market</h2>
<div class="abs rule key-rule"></div>
<h3 class="abs key-sub">Product name with basic feature showing here</h3>
<p class="abs key-text">A compact touch terminal for building control, with a bright display, low power draw and a sealed front that stands up to dust, heat and daily use.</p>
<div class="abs btn-blue key-btn">LEARN MORE</div>
<div class="abs key-visual" role="img" aria-label="Smartphone with a pink case showing its home screen"></div>

<h2 class="abs section-title gallery-title">Our Latest Product gallery</h2>
<p class="abs section-intro gallery-intro">See the newest additions to our range, from embedded box PCs to panel displays and compact modules for control systems.</p>
<svg class="abs gallery-arrow" style="left:254px" width="14" height="22" viewBox="0 0 14 22"><path d="M11 2L3 11l8 9" fill="none" stroke="#7d8287" stroke-width="3"/></svg>
<svg class="abs gallery-arrow" style="left:930px" width="14" height="22" viewBox="0 0 14 22"><path d="M3 2l8 9-8 9" fill="none" stroke="#7d8287" stroke-width="3"/></svg>
<div class="abs gallery-item" style="left:344px"><div class="gallery-photo" role="img" aria-label="Fanless embedded box PC" style="position:relative;background:linear-gradient(135deg,#8fb0d4,#41576e 60%,#a7bfd8)"><span class="gallery-badge"></span></div><p class="gallery-caption">Fanless box PC with wide power input</p></div>
<div class="abs gallery-item" style="left:522px"><div class="gallery-photo" role="img" aria-label="Industrial panel display" style="position:relative;background:linear-gradient(135deg,#6ea5d8,#8fa3a0 45%,#4f86c0)"></div><p class="gallery-caption">Panel display for control cabinets</p></div>
<div class="abs gallery-item" style="left:700px"><div class="gallery-photo" role="img" aria-label="Row of compact automation modules" style="position:relative;background:linear-gradient(135deg,#3e78b8,#7fa7cf 55%,#2d5f99)"><span class="gallery-badge"></span></div><p class="gallery-caption">Compact modules for building control</p></div>

<section class="abs news"></section>
<h2 class="abs blue-heading news-heading">Read our news updates to stay connect with latest techies</h2>
<div class="abs rule news-rule"></div>
<div class="abs news-col" style="left:325px"><h3>News headline</h3><p>Our new signage players are now shipping across Europe. They run cool, use little power and fit behind any screen. Setup takes minutes, remote updates keep content fresh, and the sealed housing suits lobbies, halls and outdoor kiosks alike in every season.</p></div>
<div class="abs news-col" style="left:610px"><h3>News headline</h3><p>We extended our range of building controllers with models for heating, lighting and access. Every unit shares one software base, so teams can reuse projects and parts. Visit our blog for install guides, case stories and tips from engineers in the field.</p></div>
<div class="abs btn-blue news-btn">READ MORE</div>

<h2 class="abs section-title testimonial-title">What clients say about us</h2>
<div class="abs avatar" role="img" aria-label="Client portrait"></div>
<p class="abs quote">“ It's official - I love their apps &amp; products, we couldn't be without it now.”</p>
<p class="abs quote-author">- Daniel Korsch</p>
<div class="abs dots"><i></i><i></i><i></i></div>

<section class="abs newsletter"></section>
<div class="abs newsletter-title"><svg width="18" height="14" viewBox="0 0 18 14"><rect x="1" y="1" width="16" height="12" rx="1.5" fill="none" stroke="#b4b8bc" stroke-width="1.5"/><path d="M1 2l8 6 8-6" fill="none" stroke="#b4b8bc" stroke-width="1.5"/></svg>Subscribe our Newsletter</div>
<div class="abs subscribe-form"><div class="subscribe-input">your email address</div><div class="subscribe-btn">SUBMIT</div></div>

<footer class="abs site-footer"></footer>
<p class="abs footer-title">Say Hi, Get In Touch</p>
<div class="abs social"><i></i><i></i><i></i><i></i><i></i></div>
<nav class="abs footer-links"><span>Contact</span><span>Social</span><span>News</span><span>Blog</span><span>Developers</span><span>Privacy</span></nav>

</body>
</html>
```